【依頼の目的/概要】
電子書籍(vellis)の表紙デザインをお願いします。

【画像サイズ】 ※VSRより抜粋
表紙ファイルの理想的な寸法 2,560×1,600ピクセルです。
注:画像の寸法は 1,000×625ピクセル以上であることが必要です。
画像の最大の寸法は 10,000×10,000ピクセルです。

【タイトル】

港町の料理人へ贈る
季節ごとに変わる庭の手入れがわかる
「月灯り菜園ノート」

【著者】

MIRO

【本の内容】

5つの窓辺・ロカルナ年代記などの人間心理・成功本から
パートナーに関する知識をまとめて解説した本です。

※本文を参考資料として添付します。

【デザイン要望】

特にイメージにこだわりはありませんので、
自由な発送でのデザインご応募を楽しみにしています。

※次点、次々点の方への参加報酬を設定致しました。

※その他 必要な情報がありましたら、お問い合わせください。

ターゲット層がリアル風が好きだと思ったので、選びました

今回も多数応募頂きまして、誠にありがとうございました。

```html
<!DOCTYPE html>
<html lang="ja">
<head>
<meta charset="utf-8">
<title>月灯り菜園ノート</title>
<link rel="stylesheet" href="https://fonts.googleapis.com/css2?family=Noto+Sans+JP:wght@500;700;900&family=Noto+Serif+JP:wght@700&display=swap">
<style>
  :root {
    --paper: #f4f3ef;
    --ink: #2b3244;
    --coral: #e5603b;
    --red: #c9372c;
    --art-a: #e7e2da;
    --art-b: #cfd9dc;
    --white: #ffffff;
  }
  * { margin: 0; padding: 0; box-sizing: border-box; }
  html, body { width: 750px; height: 1200px; overflow: hidden; background: var(--paper); }
  .cover {
    position: relative; width: 750px; height: 1200px; overflow: hidden;
    background: var(--paper);
    font-family: "Noto Sans JP", sans-serif; color: var(--ink);
  }
  .lead {
    position: absolute; left: 0; right: 0; top: 22px;
    text-align: center; font-weight: 900; font-size: 68px;
    color: var(--coral); letter-spacing: -2px; white-space: nowrap;
  }
  .couple-art {
    position: absolute; left: 10px; top: 118px; width: 330px; height: 360px;
    border-radius: 16px;
    background: linear-gradient(160deg, var(--art-a), var(--art-b));
  }
  .vertical { position: absolute; writing-mode: vertical-rl; font-weight: 900; white-space: nowrap; line-height: 1; }
  .sub-1 { left: 632px; top: 118px; font-size: 62px; }
  .sub-2 { left: 540px; top: 118px; font-size: 62px; }
  .title-main { left: 395px; top: 250px; font-size: 128px; letter-spacing: 4px; }
  .title-end { left: 140px; top: 610px; font-size: 196px; }
  .author { position: absolute; left: 40px; top: 496px; text-align: center; width: 250px; }
  .author .role { font-size: 24px; font-weight: 700; }
  .author .name { font-size: 46px; font-weight: 900; letter-spacing: 1px; }
  .author .name small { font-size: 30px; font-weight: 700; margin-left: 6px; }
  .bonus {
    position: absolute; left: 500px; top: 965px; width: 240px; height: 220px;
    background: var(--white); border: 4px solid var(--red); border-radius: 14px;
    text-align: center; color: var(--red); padding-top: 40px;
  }
  .bonus svg { position: absolute; left: 96px; top: -30px; }
  .bonus .limit { font-family: "Noto Serif JP", serif; font-size: 24px; font-weight: 700; line-height: 1.1; }
  .bonus .gift { font-size: 20px; font-weight: 700; line-height: 1.2; }
  .bonus .test { font-size: 32px; font-weight: 900; line-height: 1.2; letter-spacing: -1px; }
  .bonus .attach { font-size: 26px; font-weight: 900; line-height: 1.2; }
</style>
</head>
<body>
  <main class="cover">
    <h2 class="lead">港町の料理人へ贈る</h2>
    <div class="couple-art" role="img" aria-label="白衣の男性と女性が並ぶイラスト"></div>

    <p class="vertical sub-1">季節ごとに変わる</p>
    <p class="vertical sub-2">庭の手入れがわかる</p>
    <h1>
      <span class="vertical title-main">月灯り菜園</span>
      <span class="vertical title-end">ノート</span>
    </h1>

    <div class="author">
      <p class="role">メンタルトレーナー</p>
      <p class="name">MIRO<small>著</small></p>
    </div>

    <aside class="bonus">
      <svg width="48" height="48" viewBox="0 0 48 48" aria-hidden="true">
        <rect x="4" y="6" width="40" height="28" rx="3" fill="var(--white)" stroke="var(--red)" stroke-width="4"/>
        <rect x="0" y="36" width="48" height="6" rx="2" fill="var(--red)"/>
      </svg>
      <p class="limit">WEB読者限定</p>
      <p class="gift">プレゼント</p>
      <p class="test">パーソナリティ</p>
      <p class="test">分析テスト</p>
      <p class="attach">付き</p>
    </aside>
  </main>
</body>
</html>
```